Financial planning firm needs business card designed

Hello

I am looking to have a standard size business card designed for our agents. Attached is our logo.

Industry/Entity Type

Financial Service

Requirements
Must have
• Marcus TrellBy
• Mortgage Agent
• Investment Specialist
• Office Address: 7 Bramwell St. W., Suite K300, Hamilton, ON L9P 4Z6
• Office Ph#: (905) 462-3918 x 517
• email: mtrellby@corvantewm.example
• www.corvantewm.example
• RNTA Lic# 46390
Nice to have
• On the back maybe put:
• 8% to 12% Fixed per year! Ask me how.

```html
<!DOCTYPE html>
<html lang="en">
<head>
<meta charset="utf-8">
<title>Corvante Wealth Management – Business Card</title>
<link rel="stylesheet" href="https://fonts.googleapis.com/css2?family=Encode+Sans+Condensed:wght@400;500;700&display=swap">
<style>
  :root {
    --teal: #57c2b2;
    --teal-dark: #3f9e90;
    --ink: #2c2633;
    --paper: #ffffff;
    --backdrop: #a9a5a4;
    --text-dark: #1f1f1f;
  }
  * { box-sizing: border-box; margin: 0; padding: 0; }
  html, body { width: 1200px; height: 1184px; overflow: hidden; }
  body {
    background: var(--backdrop);
    font-family: "Encode Sans Condensed", "Arial Narrow", sans-serif;
    position: relative;
  }
  .card {
    position: absolute;
    top: 430px;
    width: 540px;
    height: 325px;
    background: var(--paper);
    overflow: hidden;
    box-shadow: 0 4px 14px rgba(0,0,0,.18);
  }
  .card--back { left: 30px; }
  .card--front { left: 630px; }

  /* Back */
  .back__band {
    position: absolute; left: 0; right: 0; top: 84px; height: 158px;
    background: var(--ink);
  }
  .back__strip { position: absolute; width: 33px; background: var(--teal); }
  .back__strip--tl { left: 0; top: 0; height: 84px; }
  .back__strip--tr { right: 0; top: 0; height: 84px; }
  .back__strip--bl { left: 0; bottom: 0; height: 83px; }
  .back__strip--br { right: 0; bottom: 0; height: 83px; }
  .back__fold { position: absolute; width: 33px; height: 14px; }
  .back__fold--tl { left: 0; top: 70px; }
  .back__fold--tr { right: 0; top: 70px; }
  .back__fold--bl { left: 0; top: 242px; }
  .back__fold--br { right: 0; top: 242px; }
  .back__tagline {
    position: absolute; left: 0; right: 0; top: 274px;
    text-align: center; font-size: 14px; color: var(--text-dark);
  }

  /* Brand lockup */
  .brand {
    position: absolute; display: flex; align-items: center; gap: 10px;
    color: var(--paper); font-weight: 500; text-transform: uppercase;
    letter-spacing: 1.5px; line-height: 1.2; white-space: nowrap;
  }
  .brand__mark { background: var(--teal); flex: none; }
  .card--back .brand { left: 50%; top: 163px; transform: translate(-50%, -50%); font-size: 20px; }
  .card--back .brand__mark { width: 30px; height: 30px; }
  .card--front .brand { left: 18px; top: 150px; font-size: 13px; letter-spacing: 1px; gap: 8px; }
  .card--front .brand__mark { width: 24px; height: 24px; }

  /* Front */
  .front__panel {
    position: absolute; left: 0; top: 0; bottom: 0; width: 225px;
    background: var(--ink);
  }
  .front__strip {
    position: absolute; left: 225px; top: 0; bottom: 0; width: 19px;
    background: var(--teal);
  }
  .front__license {
    position: absolute; left: 43px; top: 276px;
    font-size: 13px; color: var(--teal);
  }
  .agent { position: absolute; left: 301px; top: 40px; color: var(--text-dark); }
  .agent__name { font-size: 26px; font-weight: 700; line-height: 1; text-transform: uppercase; }
  .agent__title { font-size: 11px; text-transform: uppercase; line-height: 1.25; }
  .contact {
    position: absolute; left: 252px; right: 0;
    background: var(--teal);
    display: flex; align-items: center; gap: 14px;
    padding-left: 14px;
    font-size: 15px; color: var(--text-dark); line-height: 1.1;
  }
  .contact--phone { top: 105px; height: 40px; }
  .contact--email { top: 151px; height: 40px; }
  .contact--address { top: 198px; height: 44px; }
  .contact--web { top: 248px; height: 40px; }
  .contact__icon { width: 20px; height: 20px; flex: none; }
</style>
</head>
<body>

<section class="card card--back" aria-label="Card back">
  <div class="back__strip back__strip--tl"></div>
  <div class="back__strip back__strip--tr"></div>
  <div class="back__strip back__strip--bl"></div>
  <div class="back__strip back__strip--br"></div>
  <svg class="back__fold back__fold--tl" viewBox="0 0 33 14"><polygon points="0,14 33,0 33,14" fill="var(--teal-dark)"/></svg>
  <svg class="back__fold back__fold--tr" viewBox="0 0 33 14"><polygon points="0,0 33,14 0,14" fill="var(--teal-dark)"/></svg>
  <svg class="back__fold back__fold--bl" viewBox="0 0 33 14"><polygon points="0,0 33,0 33,14" fill="var(--teal-dark)"/></svg>
  <svg class="back__fold back__fold--br" viewBox="0 0 33 14"><polygon points="0,0 33,0 0,14" fill="var(--teal-dark)"/></svg>
  <div class="back__band"></div>
  <div class="brand">
    <span class="brand__mark"></span>
    <span class="brand__name">Corvante<br>Wealth Management</span>
  </div>
  <p class="back__tagline">8% to 12% Fixed per year! Ask me how</p>
</section>

<section class="card card--front" aria-label="Card front">
  <div class="front__panel"></div>
  <div class="front__strip"></div>
  <div class="brand">
    <span class="brand__mark"></span>
    <span class="brand__name">Corvante<br>Wealth Management</span>
  </div>
  <p class="front__license">RNTA Lic# 46390</p>

  <div class="agent">
    <h1 class="agent__name">Marcus TrellBy</h1>
    <p class="agent__title">Mortgage Agent</p>
    <p class="agent__title">Investment Specialist</p>
  </div>

  <div class="contact contact--phone">
    <svg class="contact__icon" viewBox="0 0 20 20" aria-hidden="true"><circle cx="10" cy="10" r="10" fill="var(--ink)"/><rect x="7" y="4.5" width="6" height="11" rx="1" fill="none" stroke="var(--teal)" stroke-width="1.2"/><circle cx="10" cy="13.5" r=".8" fill="var(--teal)"/></svg>
    <span>(905) 462-3918 x 517</span>
  </div>
  <div class="contact contact--email">
    <svg class="contact__icon" viewBox="0 0 20 20" aria-hidden="true"><circle cx="10" cy="10" r="10" fill="var(--ink)"/><rect x="5" y="6.5" width="10" height="7" fill="none" stroke="var(--paper)" stroke-width="1.1"/><polyline points="5,6.5 10,10.5 15,6.5" fill="none" stroke="var(--paper)" stroke-width="1.1"/></svg>
    <span>mtrellby@corvantewm.example</span>
  </div>
  <div class="contact contact--address">
    <svg class="contact__icon" viewBox="0 0 20 20" aria-hidden="true"><circle cx="10" cy="10" r="10" fill="var(--ink)"/><path d="M10 16 C7 12 6 10.5 6 8.5 A4 4 0 0 1 14 8.5 C14 10.5 13 12 10 16Z" fill="var(--paper)"/><circle cx="10" cy="8.5" r="1.5" fill="var(--ink)"/></svg>
    <span>7 Bramwell St. W., Suite K300<br>Hamilton, ON L9P 4Z6</span>
  </div>
  <div class="contact contact--web">
    <svg class="contact__icon" viewBox="0 0 20 20" aria-hidden="true"><circle cx="10" cy="10" r="10" fill="var(--ink)"/><g fill="none" stroke="var(--paper)" stroke-width="1"><circle cx="10" cy="10" r="5"/><ellipse cx="10" cy="10" rx="2.2" ry="5"/><line x1="5" y1="10" x2="15" y2="10"/></g></svg>
    <span>www.corvantewm.example</span>
  </div>
</section>

</body>
</html>
```